Giving Porter

Need home page design for new website. The winner will have the opportunity to design the entire site.

I have attached 3 files.

1) Sort of a site map. PLEASE do not design the home page based on this wire frame. Be creative and use your expertise.

2) Tagline and Copy for the home page. Please just greek in or make up copy for areas that do not have copy at this time.

3) The logo.
Updates

Hi everyone, I am sorry for the delay. I have been out of town on unexpected business. I will make a decision this week. Thank you all for the great designs. Dale

Industry/Entity Type

Charity

```html
<!DOCTYPE html>
<html lang="en">
<head>
<meta charset="utf-8">
<title>Giving Porter – Home</title>
<link rel="stylesheet" href="https://fonts.googleapis.com/css2?family=Ubuntu:ital,wght@0,300;0,400;0,500;1,400&display=swap">
<style>
:root{
  --green:#6fb34f;
  --green-dark:#5e9e41;
  --blue:#3e6d97;
  --ink:#333;
  --muted:#555;
  --line:#dcdcdc;
  --soft:#f0f0f0;
  --footer:#333;
  --link-blue:#2f6a9a;
}
*{box-sizing:border-box;margin:0;padding:0}
html,body{width:1134px;height:1200px;overflow:hidden}
body{background:#fff;font-family:"Ubuntu",sans-serif;color:var(--ink);border-top:5px solid var(--green);position:relative}
.wrap{width:945px;margin:0 auto}
.site-header{height:91px;display:flex;align-items:center;justify-content:space-between}
.brand{display:flex;align-items:center;gap:10px;font-size:26px;font-weight:400;color:var(--green);letter-spacing:-0.5px}
.brand-dot{width:56px;height:56px;border-radius:50%;background:var(--green)}
.main-nav{display:flex;gap:0;align-items:center;margin-top:4px}
.main-nav a{display:block;font-size:13px;color:#222;text-decoration:none;padding:0 23px;height:42px;line-height:42px}
.main-nav a.active{background:var(--green);color:#fff;border-radius:3px;width:93px;text-align:center;padding:0}
.hero{position:relative;height:403px;
  background:radial-gradient(ellipse 45% 55% at 62% 18%,#fff2c0 0%,#f0c764 22%,rgba(210,160,70,0) 60%),
  linear-gradient(180deg,#b59a52 0%,#a48a45 35%,#7c7a35 55%,#5f6a28 75%,#4b5a21 100%)}
.hero-arrow{position:absolute;top:198px;width:34px;height:34px;border-radius:50%;background:#f4f4f4;border:3px solid #d9c68d;display:flex;align-items:center;justify-content:center}
.hero-arrow.prev{left:37px}.hero-arrow.next{right:35px}
.hero-dots{position:absolute;bottom:13px;left:0;right:0;display:flex;justify-content:center;gap:9px}
.hero-dots span{width:11px;height:11px;border-radius:50%;background:#eee;border:1px solid #666}
.hero-dots span.on{background:var(--green);border-color:var(--green)}
.features{display:flex;justify-content:space-between;margin-top:21px}
.feature{width:308px;height:196px;border:1px solid var(--line);background:#fff}
.feature.first{background:var(--soft)}
.feature h2{background:var(--green);color:#fff;font-weight:400;font-size:14.5px;height:39px;line-height:39px;padding:0 9px}
.feature p{font-size:11.4px;line-height:22.7px;color:var(--muted);padding:14px 10px 0;text-align:justify;font-weight:300}
.feature .first-p{text-align:left}
.feature a{color:var(--green);text-decoration:none}
.feature.first a{color:var(--link-blue)}
.panels{display:flex;justify-content:space-between;margin-top:25px}
.panel{width:463px;height:291px;border:1px solid var(--line)}
.panel-head{background:var(--blue);height:45px;color:#fff;display:flex;align-items:center;justify-content:space-between;padding:0 13px 0 13px}
.panel-head h3{font-weight:400;font-size:18px}
.testimonial{text-align:center;padding-top:13px}
.avatar{width:80px;height:80px;border-radius:50%;margin:0 auto;background:radial-gradient(circle at 50% 45%,#d9a887 0%,#b77d5d 55%,#5b4034 100%)}
.quote{font-size:13.5px;line-height:22.7px;color:var(--muted);padding:14px 24px 0;font-weight:300}
.cite{text-align:right;font-style:italic;font-size:13px;color:#222;padding:17px 17px 0;font-family:Arial,sans-serif}
.events{padding:16px 16px 0}
.event{display:flex;gap:10px;margin-bottom:17px}
.thumb{width:148px;height:95px;flex:none}
.thumb.course{background:linear-gradient(180deg,#e9a440 0%,#8a7a2e 38%,#3f7a2c 60%,#2e6a22 100%)}
.thumb.players{background:linear-gradient(180deg,#9cc0dc 0%,#bcc9b6 40%,#6b9a4a 75%,#557c38 100%)}
.event h4{font-weight:400;font-size:14px;color:#111;margin-top:4px}
.event p{font-size:11.2px;line-height:17px;color:var(--muted);margin-top:2px}
.event a{display:block;font-size:12px;color:#111;text-decoration:none;margin-top:2px}
.site-footer{position:absolute;left:0;right:0;top:1065px;bottom:0;background:var(--footer);color:#eee}
.site-footer .wrap{display:flex;justify-content:space-between;padding-top:37px}
.foot-links{font-size:16.5px;font-weight:300}
.foot-links a{color:#eee;text-decoration:none}
.foot-links .sep{margin:0 8px}
.copy{font-size:12.5px;margin-top:9px;font-weight:300}
.social{display:flex;gap:8px;margin-top:15px;margin-right:2px}
.social span{width:23px;height:23px;border-radius:2px}
</style>
</head>
<body>
<div class="wrap">
  <header class="site-header">
    <div class="brand"><span class="brand-dot"></span>GivingPorter.com</div>
    <nav class="main-nav">
      <a class="active" href="#">Pricing</a>
      <a href="#">Features</a>
      <a href="#">Services</a>
      <a href="#">Products</a>
      <a href="#">About</a>
      <a href="#">Contact</a>
    </nav>
  </header>

  <section class="hero" role="img" aria-label="Sunlit golf green with a hand placing a golf ball at the cup">
    <span class="hero-arrow prev"><svg width="12" height="14" viewBox="0 0 12 14"><path d="M8 2 3 7l5 5" fill="none" stroke="#333" stroke-width="2.6"/></svg></span>
    <span class="hero-arrow next"><svg width="12" height="14" viewBox="0 0 12 14"><path d="M4 2l5 5-5 5" fill="none" stroke="#333" stroke-width="2.6"/></svg></span>
    <div class="hero-dots"><span class="on"></span><span></span><span></span></div>
  </section>

  <section class="features">
    <article class="feature first">
      <h2>Raise Money. Lower Stress</h2>
      <p class="first-p">Charity golf events are proven to be an effective way to raise money for worthy causes. But who has the time to manage all the details? You do now, with Giving Porter.<br><a href="#">Learn more</a></p>
    </article>
    <article class="feature">
      <h2>Everything You Need In One Place.</h2>
      <p>We are experienced in both the art of fundraising as well as the dynamics of a golf event and we are here to help you. We offer everything from simple self-service tools that include professionally-designed website and email templates all the way up to full service event planning. &nbsp;<a href="#">Learn more</a></p>
    </article>
    <article class="feature">
      <h2>Sold! Silent Auction Items Add More $!</h2>
      <p>Exclusive to GivingPorter.com is our Silent Auction module. Through our partners we can add even more value to your golf event. Auction off premium items during the tournament and add to your fundraising!<br><a href="#">Learn more</a></p>
    </article>
  </section>

  <section class="panels">
    <article class="panel">
      <div class="panel-head"><h3>Testimonials</h3>
        <svg width="24" height="16" viewBox="0 0 24 16"><path d="M8 2 3 8l5 6M16 2l5 6-5 6" fill="none" stroke="#fff" stroke-width="2.2"/></svg></div>
      <div class="testimonial">
        <div class="avatar" role="img" aria-label="Portrait of the client giving the testimonial"></div>
        <p class="quote">Donec sed odio dui. Nullam id dolor id nibh ultricies vehicula ut id elit. Sollicitudin Lorem Egestas Dapibus. Donec sed odio dui. Nullam id dolor id nibh ultricies vehicula ut id elit.</p>
        <p class="cite">- Arlen</p>
      </div>
    </article>
    <article class="panel">
      <div class="panel-head"><h3>Seminars and Events</h3>
        <svg width="24" height="16" viewBox="0 0 24 16"><path d="M8 2 3 8l5 6M16 2l5 6-5 6" fill="none" stroke="#fff" stroke-width="2.2"/></svg></div>
      <div class="events">
        <div class="event">
          <div class="thumb course" role="img" aria-label="Golf ball at the cup on a green at sunset"></div>
          <div><h4>Lorem ipsum</h4>
            <p>Lorem ipsum dolor sit amet, consectetuer adipiscing elit, sed diam nonummy nibh euismod tincidunt ut laoreet dolore magna aliquam erat volutpat.</p>
            <a href="#">Read More...</a></div>
        </div>
        <div class="event">
          <div class="thumb players" role="img" aria-label="Group of golfers shaking hands on the course"></div>
          <div><h4>Energy Efficiency</h4>
            <p>Lorem ipsum dolor sit amet, consectetuer adipiscing elit, sed diam nonummy nibh euismod tincidunt ut laoreet dolore magna aliquam erat volutpat.</p>
            <a href="#">Read More...</a></div>
        </div>
      </div>
    </article>
  </section>
</div>

<footer class="site-footer">
  <div class="wrap">
    <div>
      <nav class="foot-links"><a href="#">Home</a><span class="sep">|</span><a href="#">About Us</a><span class="sep">|</span><a href="#">Serives</a><span class="sep">|</span><a href="#">Contact Us</a><span class="sep">|</span><a href="#">Blog</a></nav>
      <p class="copy">© 2014 Company Name &nbsp;All right reserved &nbsp;Term of Use</p>
    </div>
    <div class="social" aria-label="Social links">
      <span style="background:#4a67a8"></span>
      <span style="background:#5fb8e6"></span>
      <span style="background:#1f7bbd"></span>
      <span style="background:#f08a24"></span>
    </div>
  </div>
</footer>
</body>
</html>
```